Construction company that specializes in roofing and siding

https://havenridgeroofs.example/featured-projects/

https://www.pinecrestrenovationllc.example/#

https://www.ironmeadowhomes.example/residential-siding-services/

Please model a website after these examples
I posted a doc that has some content to get you started. I will upload more content and photos as the site progresses.

Coded - Design and coding required

5+ page

```html
<!DOCTYPE html>
<html lang="en">
<head>
<meta charset="utf-8">
<title>Stoneridge Construction — Roofing &amp; Siding in Minnesota</title>
<link rel="stylesheet" href="https://fonts.googleapis.com/css2?family=Rubik:wght@400;500;700&family=Nunito+Sans:wght@400;600;700;800&display=swap">
<style>
  :root{
    --blue:#2c49ad;
    --blue-dark:#23398c;
    --orange:#f5945a;
    --ink:#2b2f3a;
    --muted:#5a5f6b;
    --line:#dcdfe5;
    --grey-band:#e4e4e4;
    --white:#ffffff;
  }
  *{box-sizing:border-box;margin:0;padding:0}
  html,body{width:1200px;height:3935px;overflow:hidden}
  body{position:relative;background:var(--white);font-family:"Nunito Sans",sans-serif;color:var(--ink)}
  .abs{position:absolute}
  h1,h2,h3,.display{font-family:"Rubik",sans-serif}

  /* header */
  .site-header{left:0;top:0;width:1200px;height:72px;background:var(--white)}
  .brand{left:96px;top:22px;display:flex;align-items:center;gap:8px;font-family:"Rubik",sans-serif;font-weight:700;font-size:15px;color:#3b3f48;letter-spacing:.5px}
  .brand-mark{width:26px;height:26px;border-radius:50%;background:#3b3f48}
  .nav a{position:absolute;top:29px;font-size:13px;color:#6a6e78;text-decoration:none;white-space:nowrap}

  /* hero */
  .hero{left:0;top:72px;width:1200px;height:533px;background:linear-gradient(180deg,#3b4a60 0%,#4d5566 45%,#6b5a48 80%,#3a3630 100%)}
  .hero-title{left:200px;top:140px;width:800px;text-align:center;color:var(--white);font-family:"Rubik",sans-serif;font-weight:400;font-size:50px;line-height:59px}
  .hero-title b{font-weight:700}
  .feature-box{left:843px;top:446px;width:347px;height:125px;background:var(--blue);color:var(--white);text-align:center;padding-top:36px}
  .feature-box h3{font-size:23px;font-weight:700}
  .feature-box p{font-size:13px;margin-top:8px}
  .feature-nav{left:843px;top:571px;width:347px;height:34px;background:#2e3440;display:flex;justify-content:center;align-items:center;gap:20px}

  /* reputation */
  .section-title{color:var(--blue);font-weight:700;font-size:41px;text-align:center}
  .rep-card{top:741px;width:243px;height:146px;border:1px solid var(--line);padding:28px 16px 0}
  .rep-card h4{font-size:15px;font-weight:800;color:#3b3f48;margin-top:6px}
  .rep-card p{font-size:13px;color:var(--muted);line-height:21px;margin-top:4px}

  /* about */
  .about-photo{left:105px;top:993px;width:597px;height:529px;background:linear-gradient(135deg,#c9b98a 0%,#e88a2e 40%,#f0b03a 60%,#d8d4cc 100%);box-shadow:0 10px 20px rgba(0,0,0,.18)}
  .about-panel{left:702px;top:993px;width:405px;height:435px;background:var(--blue);color:var(--white);padding:38px 30px 0 29px;box-shadow:0 10px 20px rgba(0,0,0,.12)}
  .about-panel h2{font-size:29px;font-weight:700}
  .about-panel p{font-size:16px;line-height:21px;margin-top:21px}
  .btn-light{display:inline-block;margin-top:24px;background:var(--white);color:var(--blue);font-weight:800;font-size:14px;padding:10px 9px;border-radius:3px}

  /* stats */
  .stat{background:var(--white);box-shadow:0 4px 14px rgba(0,0,0,.12);padding:14px 0 0 26px}
  .stat .num{font-family:"Rubik",sans-serif;font-weight:500;font-size:54px;color:var(--ink);line-height:60px}
  .stat .label{font-size:20px;color:var(--muted);border-left:4px solid var(--orange);padding-left:12px;margin-top:4px;line-height:22px}
  .stat-icon{border-radius:10px}
  .exp-title{left:789px;top:1610px;color:var(--blue);font-weight:700;font-size:48px;line-height:58px}
  .exp-text{left:789px;top:1736px;width:300px;font-size:16px;line-height:21px;color:var(--muted)}
  .btn-blue{background:var(--blue);color:var(--white);font-weight:800;font-size:14px;text-align:center;border-radius:3px}

  /* consultation band */
  .cta-band{left:0;top:2084px;width:1200px;height:249px;background:linear-gradient(90deg,#2b2b2d 0%,#4a4a4c 50%,#3a3a3c 100%)}
  .cta-title{left:93px;top:2166px;color:var(--white);font-weight:700;font-size:29px}
  .cta-line{left:93px;top:2227px;color:var(--white);font-size:20px}
  .cta-line u{text-underline-offset:3px}
  .btn-outline{left:789px;top:2177px;width:196px;height:42px;border:1px solid var(--white);border-radius:4px;color:var(--white);font-weight:800;font-size:14px;text-align:center;line-height:40px}

  /* projects */
  .projects-title{left:111px;top:2403px;font-size:29px;font-weight:700;color:var(--ink)}
  .filter{left:128px;font-size:20px;color:var(--muted)}
  .filter.active{color:var(--blue);font-weight:800;left:111px;border-left:4px solid var(--blue);padding-left:13px;line-height:22px}
  .project{width:320px}
  .project .img{height:206px}
  .project .cap{background:var(--blue);color:var(--white);height:73px;padding:10px 10px 0}
  .project h3{font-size:20px;font-weight:700}
  .project p{font-size:14px;margin-top:6px}

  /* contact */
  .meet{left:0;top:3058px;width:1200px;height:530px;background:var(--grey-band)}
  .meet-sub{left:350px;top:3164px;width:500px;text-align:center;font-size:17px;line-height:21px;color:#444}
  .field{background:var(--white);border:1px solid #c9c9c9;font-size:14px;color:#888;padding:6px 6px}
  .field i{color:#e0323a;font-style:normal}
  .note{left:354px;top:3452px;font-size:12px;color:#777}
  .note i{color:#e0323a;font-style:normal}

  /* footer */
  .f-label{font-size:13px;font-weight:800;color:var(--blue);letter-spacing:.5px}
  .f-value{font-size:16px;color:#444;line-height:20px}
  .social{width:32px;height:32px;border-radius:50%;background:#2f3340}
  .copyright{left:0;top:3874px;width:1200px;height:61px;background:var(--blue);color:var(--white);text-align:center;font-size:13px;line-height:61px}
</style>
</head>
<body>

<header class="abs site-header">
  <div class="abs brand"><span class="brand-mark"></span>STONERIDGE</div>
  <nav class="nav">
    <a style="left:360px">Home</a>
    <a style="left:444px">About</a>
    <a style="left:528px">Roofing ▾</a>
    <a style="left:621px">Siding ▾</a>
    <a style="left:707px">Gutters</a>
    <a style="left:800px">Windows</a>
    <a style="left:904px">Repair ▾</a>
    <a style="left:991px">Storm Damage Repair ▾</a>
  </nav>
</header>

<section class="abs hero" role="img" aria-label="Two-storey family home with lit windows and a double garage at dusk"></section>
<h1 class="abs hero-title"><b>Stoneridge Construction</b> is your source <b>for roofing</b> and siding <b>in Minnesota.</b></h1>
<div class="abs feature-box"><h3>Feature Projects</h3><p>Lakeside Community Library</p></div>
<div class="abs feature-nav">
  <svg width="18" height="14" viewBox="0 0 18 14" fill="none" stroke="#fff" stroke-width="1.8"><path d="M17 7H2M7 1L1 7l6 6"/></svg>
  <svg width="18" height="14" viewBox="0 0 18 14" fill="none" stroke="#fff" stroke-width="1.8"><path d="M1 7h15M11 1l6 6-6 6"/></svg>
</div>

<h2 class="abs section-title" style="left:0;top:662px;width:1200px">Stoneridge Construction Reputation</h2>

<div class="abs rep-card" style="left:180px">
  <svg width="24" height="24" viewBox="0 0 24 24" fill="none" stroke="#222" stroke-width="2"><circle cx="12" cy="12" r="10"/><circle cx="12" cy="12" r="6"/><circle cx="12" cy="12" r="2" fill="#222"/></svg>
  <h4>Our Mission</h4><p>Nullam senectus porttitor in eget. Eget rutrum leo interdum.</p>
</div>
<div class="abs rep-card" style="left:479px">
  <svg width="34" height="24" viewBox="0 0 34 24" fill="none" stroke="#222" stroke-width="2.2"><path d="M2 12C8 3 26 3 32 12C26 21 8 21 2 12Z"/><circle cx="17" cy="12" r="4.5" fill="#222"/></svg>
  <h4>Our Vision</h4><p>Nullam senectus porttitor in eget. Eget rutrum leo interdum.</p>
</div>
<div class="abs rep-card" style="left:780px">
  <svg width="28" height="24" viewBox="0 0 28 24" fill="#222"><rect x="2" y="16" width="5" height="8"/><rect x="9" y="12" width="5" height="12"/><rect x="16" y="9" width="5" height="15"/><rect x="23" y="5" width="5" height="19"/><path d="M2 12L10 6l5 3 9-7" stroke="#222" stroke-width="2" fill="none"/></svg>
  <h4>Our Value</h4><p>Nullam senectus porttitor in eget. Eget rutrum leo interdum.</p>
</div>

<div class="abs about-photo" role="img" aria-label="Three builders in hard hats and safety vests reviewing plans"></div>
<div class="abs about-panel">
  <h2>About us</h2>
  <p>From humble beginnings:</p>
  <p>In 2016 Dale Harmon started helping people with their home improvement projects.</p>
  <p>His very first job was installing window trim for a wonderful homeowner in Forest lake MN.</p>
  <p>He did his best work and made sure he treated his first customer like family.</p>
  <span class="btn-light">More on Our History</span>
</div>

<div class="abs stat" style="left:428px;top:1573px;width:233px;height:122px"><div class="num">84</div><div class="label">Happy Clients</div></div>
<div class="abs stat-icon" style="left:606px;top:1556px;width:76px;height:76px;background:linear-gradient(135deg,#4aa3f0,#f5a45a)" role="img" aria-label="Handshake illustration"></div>
<div class="abs stat" style="left:177px;top:1664px;width:301px;height:115px;padding-top:10px"><div class="num">123</div><div class="label">Projects Completed</div></div>
<div class="abs stat-icon" style="left:203px;top:1588px;width:64px;height:69px;background:linear-gradient(135deg,#e8ecf3,#5a9ee8)" role="img" aria-label="Document and pen illustration"></div>
<div class="abs stat" style="left:382px;top:1779px;width:230px;height:119px"><div class="num">37</div><div class="label">Awards Win</div></div>
<div class="abs stat-icon" style="left:554px;top:1759px;width:74px;height:74px;background:linear-gradient(135deg,#f5a94a,#5aa8f0)" role="img" aria-label="Trophy held in hands illustration"></div>
<div class="abs stat" style="left:195px;top:1921px;width:278px;height:122px"><div class="num">30</div><div class="label">Years in Business</div></div>
<div class="abs stat-icon" style="left:460px;top:1955px;width:68px;height:66px;background:linear-gradient(135deg,#5aa8f0,#f07a4a)" role="img" aria-label="Floor plan and pencil illustration"></div>

<h2 class="abs exp-title">30 Years<br>Experience</h2>
<p class="abs exp-text">Our company has been the leading provided construction services to clients throughout the USA since 1988.</p>
<div class="abs btn-blue" style="left:789px;top:1845px;width:165px;height:41px;line-height:41px">Contact Us</div>

<section class="abs cta-band" role="img" aria-label="Modern kitchen interior in dark tones"></section>
<h2 class="abs cta-title">Free consultation with exceptional quality</h2>
<p class="abs cta-line">Just one call away: <u>+1 555 014 2290</u></p>
<div class="abs btn-outline">Get your consultation</div>

<h2 class="abs projects-title">Projects</h2>
<div class="abs filter active" style="top:2472px">All</div>
<div class="abs filter" style="top:2510px">Commercial</div>
<div class="abs filter" style="top:2550px">Residential</div>
<div class="abs filter" style="top:2590px">Other</div>

<article class="abs project" style="left:440px;top:2411px">
  <div class="img" role="img" aria-label="Roofer working on a red tile roof" style="background:linear-gradient(160deg,#d6544a,#b83a33 60%,#e8e4dc)"></div>
  <div class="cap"><h3>Roofing</h3><p>In MN you should expect to get...</p></div>
</article>
<article class="abs project" style="left:788px;top:2411px">
  <div class="img" role="img" aria-label="Green sided house with white porch" style="background:linear-gradient(180deg,#b8cde4,#8a9a6a 55%,#6d7d50)"></div>
  <div class="cap"><h3>Siding</h3><p>In MN you should expect to get...</p></div>
</article>
<article class="abs project" style="left:440px;top:2714px">
  <div class="img" role="img" aria-label="Worker installing a white gutter downspout" style="background:linear-gradient(160deg,#c85a48,#e6e2dc 50%,#9a9690)"></div>
  <div class="cap"><h3>Gutters</h3><p>In MN you should expect to get...</p></div>
</article>
<article class="abs project" style="left:788px;top:2714px">
  <div class="img" role="img" aria-label="Brick house damaged by a fallen tree" style="background:linear-gradient(160deg,#8a5a40,#b56a48 50%,#6a5a48)"></div>
  <div class="cap"><h3>Storm Damage Repair</h3><p>In MN you should expect to get...</p></div>
</article>

<section class="abs meet"></section>
<h2 class="abs section-title" style="left:0;top:3100px;width:1200px;font-size:42px">Let’s Meet</h2>
<p class="abs meet-sub">We are ready to work on a project of any complexity, whether it’s commercial or residential.</p>
<div class="abs field" style="left:354px;top:3234px;width:232px;height:32px">Your Name<i>*</i></div>
<div class="abs field" style="left:614px;top:3234px;width:232px;height:32px">Email<i>*</i></div>
<div class="abs field" style="left:354px;top:3284px;width:232px;height:32px">Reason for Contacting<i>*</i>
  <svg class="abs" style="right:6px;top:9px" width="14" height="14" viewBox="0 0 14 14"><circle cx="7" cy="7" r="7" fill="var(--blue)"/><path d="M4 6l3 3 3-3" stroke="#fff" stroke-width="1.6" fill="none"/></svg>
</div>
<div class="abs field" style="left:614px;top:3284px;width:232px;height:32px">Phone</div>
<div class="abs field" style="left:354px;top:3335px;width:492px;height:110px">Message</div>
<p class="abs note"><i>*</i> indicates a required field</p>
<div class="abs btn-blue" style="left:489px;top:3492px;width:224px;height:43px;line-height:43px;border-radius:0">SUBMIT</div>

<div class="abs f-label" style="left:93px;top:3647px">ADDRESS:</div>
<div class="abs f-value" style="left:180px;top:3644px">1280 Birchwood Ave. Duluth,<br>Minnesota 55802</div>
<div class="abs f-label" style="left:93px;top:3711px">PHONE:</div>
<div class="abs f-value" style="left:180px;top:3708px">+1 555 014 2290</div>
<div class="abs f-label" style="left:93px;top:3757px">EMAIL:</div>
<div class="abs f-value" style="left:180px;top:3754px">hello@stoneridge.example</div>

<div class="abs f-label" style="left:754px;top:3647px">NEWSLETTER:</div>
<div class="abs field" style="left:754px;top:3681px;width:232px;height:33px;border-color:#ddd">Your email here</div>
<div class="abs" style="left:994px;top:3681px;width:113px;height:33px;background:var(--orange);color:#fff;font-weight:800;font-size:14px;text-align:center;line-height:33px;border-radius:2px">Subscribe</div>
<div class="abs f-label" style="left:754px;top:3752px">SOCIAL:</div>
<div class="abs social" style="left:754px;top:3787px"></div>
<div class="abs social" style="left:805px;top:3787px"></div>
<div class="abs social" style="left:855px;top:3787px"></div>

<footer class="abs copyright">© 2024 Stoneridge. All Rights Reserved</footer>

</body>
</html>
```